Lebel for 500g Honey Jar

We want a design for a 500g honey bottle or Jar as shown in the attached image . All Requirement has been put in the attached brief document .
Also Logo and images have been uploaded . Feel free to play arround with the selected solor schemes .

Target Market(s)

Retail Market

Industry/Entity Type

FMCG

Colors
00AB8E
00BBA5
67D7C9
C6EFE9
E9F9F6
59FF00
82FF00
B8FF75
E3FFCB
F4FFEA
FFC000
F8CF3A
FAE287
FDF2CF
FEFAEE
F0912C
F2A743
F7CA91
FBE8D2
FDF5EE
EE7325
F08F49
F5BC92
FAE3D3
FDF4ED

Requirements
Must have
• The desing must contain the company Address, Logo , and Nutritional Facts
Nice to have
• Image of a honey Bee , see samples attahed

```html
<!DOCTYPE html>
<html lang="en">
<head>
<meta charset="utf-8">
<title>Meadowly Pure Honey – Front Bottle Label</title>
<link href="https://fonts.googleapis.com/css2?family=Great+Vibes&family=Kalam:wght@400&family=Oswald:wght@400;500&family=Playfair+Display:wght@700&family=Roboto:ital,wght@1,900&display=swap" rel="stylesheet">
<style>
  :root {
    --honey: #f9b912;
    --honey-deep: #f6a80c;
    --honey-light: #fdd94a;
    --cream: #fefaee;
    --cream-warm: #fbefc9;
    --leaf: #6f9160;
    --leaf-band: #7a9a66;
    --ink: #111111;
    --white: #ffffff;
  }
  * { box-sizing: border-box; margin: 0; padding: 0; }
  html, body { width: 1200px; height: 1200px; overflow: hidden; background: var(--white); }
  .canvas { position: relative; width: 1200px; height: 1200px; background: var(--white); }

  .label {
    position: absolute; left: 133px; top: 99px; width: 631px; height: 1009px;
    background: radial-gradient(ellipse at 50% 45%, var(--honey-light) 0%, var(--honey) 55%, var(--honey-deep) 100%);
    overflow: hidden;
  }
  .label__panel-svg { position: absolute; left: 0; top: 0; }

  .brand {
    position: absolute; left: 0; width: 631px; top: 118px; text-align: center;
    font-family: 'Oswald', sans-serif; font-weight: 500; font-size: 50px;
    color: var(--ink); letter-spacing: 1px;
  }

  .art { position: absolute; border-radius: 50%; }
  .art--left {
    left: 42px; top: 200px; width: 212px; height: 172px;
    background: radial-gradient(circle at 50% 50%, #f6b12a 0%, #f3a520 30%, #7f9f6d 55%, rgba(127,159,109,0) 72%);
  }
  .art--right {
    left: 398px; top: 485px; width: 250px; height: 259px;
    background: radial-gradient(circle at 58% 50%, #f6b12a 0%, #f3a520 32%, #7f9f6d 55%, rgba(127,159,109,0) 72%);
  }

  .title-script {
    position: absolute; left: 250px; top: 255px;
    font-family: 'Great Vibes', cursive; font-size: 112px; color: var(--leaf); line-height: 1;
  }
  .title-main {
    position: absolute; left: 0; width: 631px; top: 355px; text-align: center;
    font-family: 'Playfair Display', serif; font-weight: 700; font-size: 152px;
    color: var(--honey); line-height: 1; letter-spacing: -2px;
    text-shadow: 2px 2px 3px rgba(0,0,0,0.25);
  }

  .claim {
    position: absolute; text-align: center; white-space: nowrap;
    font-family: 'Great Vibes', cursive; color: var(--leaf); line-height: 1;
    text-shadow: 1px 1px 2px rgba(0,0,0,0.25);
  }
  .claim--percent { top: 550px; left: 60px; width: 320px; font-size: 62px; }
  .claim--natural { top: 612px; left: 60px; width: 340px; font-size: 56px; }

  .badge {
    position: absolute; top: 710px; width: 144px; height: 144px; border-radius: 50%;
    background: var(--honey); border: 5px solid var(--white);
    box-shadow: 2px 3px 6px rgba(0,0,0,0.3);
    display: flex; flex-direction: column; align-items: center; justify-content: center;
    font-family: 'Oswald', sans-serif; font-weight: 400; color: var(--white);
    font-size: 26px; line-height: 1.15; text-align: center;
    text-shadow: 1px 1px 2px rgba(0,0,0,0.3);
  }
  .badge--additive { left: 59px; }
  .badge--colouring { left: 245px; }
  .badge--preservative { left: 431px; font-size: 23px; }

  .distributor {
    position: absolute; left: 0; top: 895px; width: 631px; height: 51px;
    background: var(--leaf-band); color: var(--white);
    display: flex; align-items: center; justify-content: center;
    font-family: 'Kalam', cursive; font-size: 25px; white-space: nowrap;
  }
  .net-weight {
    position: absolute; left: 0; width: 631px; top: 954px; text-align: center;
    font-family: 'Oswald', sans-serif; font-weight: 500; font-size: 32px; color: var(--ink);
  }

  .caption {
    position: absolute; left: 861px; top: 430px; width: 260px; text-align: center;
    font-family: 'Roboto', sans-serif; font-style: italic; font-weight: 900;
    font-size: 22px; line-height: 28px; color: var(--ink);
  }

  .mockup {
    position: absolute; left: 853px; top: 606px; width: 266px; height: 563px;
    border-radius: 110px 110px 60px 60px;
    background: linear-gradient(180deg, #f2f3f4 0%, #fbe9a8 30%, #f9c733 70%, #f1f1f1 88%, #ffe000 100%);
  }
</style>
</head>
<body>
<div class="canvas">
  <section class="label">
    <svg class="label__panel-svg" width="631" height="1009" viewBox="0 0 631 1009" aria-hidden="true">
      <defs>
        <linearGradient id="panelFill" x1="0" y1="0" x2="0" y2="1">
          <stop offset="0" stop-color="#fefcf2"/>
          <stop offset="0.55" stop-color="#fbf0cd"/>
          <stop offset="1" stop-color="#fefaee"/>
        </linearGradient>
      </defs>
      <path d="M23 895 V157 H153 C175 90 240 57 318 57 C396 57 461 90 483 157 H610 V895 Z"
            fill="url(#panelFill)" stroke="#fbe7a4" stroke-width="3"/>
    </svg>

    <div class="brand">Meadowly</div>

    <div class="art art--left" role="img" aria-label="Honeycomb cluster with a honey bee framed by green leaves"></div>
    <div class="art art--right" role="img" aria-label="Honeycomb cluster with a honey bee framed by green leaves"></div>

    <div class="title-script">Pure</div>
    <h1 class="title-main">HONEY</h1>

    <p class="claim claim--percent">100%</p>
    <p class="claim claim--natural">Pure &amp; Natural</p>

    <div class="badge badge--additive"><span>ZERO</span><span>ADDITIVE</span></div>
    <div class="badge badge--colouring"><span>ZERO</span><span>COLOURING</span></div>
    <div class="badge badge--preservative"><span>ZERO</span><span>PRESERVATIVE</span></div>

    <div class="distributor">Packed &amp; Distributed by Fieldhouse Farms Limited</div>
    <div class="net-weight">Net WT: 500g</div>
  </section>

  <p class="caption">Meadowly<br>Pure Honey<br>Front bottle label</p>

  <div class="mockup" role="img" aria-label="Clear squeeze bottle with a yellow cap carrying the front label"></div>
</div>
</body>
</html>
```